Luxury Brand Real Estate For Sale sign

**Update** I've added some examples from the internet of other signs that have a look similar to what I would like to see. I do not want my personal name in the sign. And the word FOR SALE Does not need to be so large - it can be more subtle.
I want to create a Real Estate for sale sign for my company that will be used for luxury/higher end real estate listings. I’m sharing my business card as well as a logo with new teal color to show what we're moving towards: we’re using Teal, white, black and gold.
Hoping the sign is simple, sophisticated and eye catching.
The sign should be 24" wide by 30" tall including the company name: Harbor Crest Realty Group and our logo, office phone number 727-555-0148 and website www.hcrgexample.com the words "For Sale"
Optional to add this e-mail address info@hcrgexample.com to the sign
Target Market(s)
Luxury home buyers
Industry/Entity Type
Real Estate
Look and feel

```html
<!DOCTYPE html>
<html lang="en">
<head>
<meta charset="utf-8">
<title>Harbor Crest Realty Group – For Sale Sign</title>
<link rel="stylesheet" href="https://fonts.googleapis.com/css2?family=Cinzel:wght@700&family=Poppins:wght@300;400;600&display=swap">
<style>
  :root {
    --teal: #05827f;
    --gold-light: #fbe79a;
    --gold: #e0ad3a;
    --gold-deep: #c99427;
    --band: #eceff0;
    --band-shade: #dfe6e7;
    --white: #ffffff;
    --page: #f4f4f2;
  }
  * { margin: 0; padding: 0; box-sizing: border-box; }
  html, body {
    width: 1190px;
    height: 1200px;
    overflow: hidden;
    background: var(--page);
  }
  .canvas {
    width: 1190px;
    height: 1200px;
    display: flex;
    align-items: center;
    justify-content: center;
  }
  .sign {
    position: relative;
    width: 880px;
    height: 1100px;
    background: var(--teal);
    overflow: hidden;
  }
  .headline {
    position: absolute;
    left: 88px;
    top: 70px;
    font-family: "Cinzel", serif;
    font-weight: 700;
    font-size: 250px;
    line-height: 228px;
    letter-spacing: -4px;
    background: linear-gradient(180deg, var(--gold-deep) 0%, var(--gold-light) 45%, var(--gold) 100%);
    -webkit-background-clip: text;
    background-clip: text;
    color: transparent;
  }
  .contact {
    position: absolute;
    left: 86px;
    top: 640px;
    color: var(--white);
    font-family: "Poppins", sans-serif;
  }
  .contact-phone {
    display: flex;
    align-items: center;
    gap: 12px;
    font-weight: 600;
    font-size: 84px;
    line-height: 1;
    letter-spacing: -1px;
  }
  .contact-phone svg { width: 60px; height: 60px; flex: none; }
  .contact-web {
    margin-top: 8px;
    font-weight: 400;
    font-size: 50px;
    letter-spacing: 5px;
  }
  .brand-band {
    position: absolute;
    left: 0;
    top: 820px;
    width: 100%;
    height: 280px;
    background: var(--band);
  }
  .brand-band-art {
    position: absolute;
    inset: 0;
    background: radial-gradient(ellipse at 70% 55%, var(--white) 0%, var(--white) 30%, var(--band-shade) 70%, var(--band) 100%);
  }
  .brand {
    position: absolute;
    left: 86px;
    top: 70px;
    display: flex;
    align-items: center;
    gap: 28px;
    height: 150px;
  }
  .brand-square {
    width: 44px;
    height: 44px;
    background: var(--gold);
  }
  .brand-divider {
    width: 3px;
    height: 150px;
    background: var(--gold);
  }
  .brand-name {
    font-family: "Poppins", sans-serif;
    font-weight: 300;
    font-size: 44px;
    line-height: 1.15;
    letter-spacing: 1px;
    color: var(--gold-deep);
    text-transform: uppercase;
  }
</style>
</head>
<body>
  <main class="canvas">
    <section class="sign">
      <h1 class="headline">FOR<br>SALE</h1>

      <div class="contact">
        <div class="contact-phone">
          <svg viewBox="0 0 60 60" aria-hidden="true">
            <circle cx="30" cy="30" r="29" fill="#ffffff"/>
            <path d="M22 16c2 0 3 1 4 4l1 4c0 2-1 3-3 4 2 5 5 8 10 10 1-2 2-3 4-3l4 1c3 1 4 2 4 4v3c0 2-2 3-4 3-14-1-24-11-25-25 0-3 2-5 5-5z" fill="#05827f"/>
          </svg>
          <span>727-555-0148</span>
        </div>
        <div class="contact-web">www.hcrgexample.com</div>
      </div>

      <div class="brand-band">
        <div class="brand-band-art" role="img" aria-label="Faint light map of the coastline behind the company name"></div>
        <div class="brand">
          <div class="brand-square"></div>
          <div class="brand-divider"></div>
          <div class="brand-name">Harbor Crest<br>Realty Group</div>
        </div>
      </div>
    </section>
  </main>
</body>
</html>
```